Plakate Musikalischer Rückblick eines Italienischen Musikers
Zielgruppe
Wir brauchen ein Plakat mit dem man Veranstalter überzeugen kann Tickets in allen Altersklassen (30+) zu verkaufen.
Der Titel ist: Ventoro
Untertittel: Ein Musikalischer Rückblick eines Italienischen Musikers.
Hier ein Link zu einem Video. Das erklärt, glaube ich alles über das Projekt. https://clipvaro.net/Rk3Tm9Qp2Zs?si=Hb7NcLq4Wy81VtxA
Im Anhang sind 2 Plakate. Beide gefallen mir nicht wirklich.
Grund Plakat 1: Das Plakat ist schön aber man sieht sofort das es KI ist. Mir ist es auch ein bisschen zu viel Klischee und zu wenig Musik.
Grund Plakat 2: Ästhetisch ist es ohne Zweifel besser. Allerdings habe ich ein bisschen das Gefühl, dass es die falschen Erwartungen weckt. Ich finde die Idee gut, sich von allzu touristischen Klischees fernzuhalten. Trotzdem würde ich mir eher Dynamik und Leidenschaft wünschen, statt einer zu träumerisch-melancholischen Stimmung. Kurz gesagt: Für meinen Geschmack dürfte es ruhig etwas lebendiger sein. Die Noten sind generell OK, sehen aber nicht gut aus da dieses verblassen. Die Effekte oben, Sonne, Feuerwerk würde ich weglassen.
Aufgabenstellung
Bitte offene Datei als PS oder ID
Bitte kein KI benutzen.
Ich freue mich auf die Vorschläge

```html
<!DOCTYPE html>
<html lang="de">
<head>
<meta charset="utf-8">
<title>Ventoro – Plakat</title>
<link rel="stylesheet" href="https://fonts.googleapis.com/css2?family=Cormorant+Garamond:wght@600&family=Arimo:wght@400;500;700&display=swap">
<style>
  :root {
    --page-bg: #7f7f7f;
    --poster-bg: #0c0c0e;
    --flag-green: #2f6b45;
    --flag-white: #8a8a8c;
    --flag-red: #8a3a2c;
    --text-light: #ffffff;
    --text-soft: #f1eef2;
    --photo-top: #3a2a28;
    --photo-mid: #1f2a44;
    --photo-low: #0e1118;
  }
  * { margin: 0; padding: 0; box-sizing: border-box; }
  html, body { width: 1000px; height: 1200px; overflow: hidden; background: var(--page-bg); }
  .poster {
    position: absolute; left: 76px; top: 0; width: 848px; height: 1200px;
    background: var(--poster-bg); overflow: hidden;
    font-family: "Arimo", Arial, sans-serif; color: var(--text-light);
  }
  .flag-band { position: absolute; top: 0; }
  .flag-band--green { left: 0; width: 250px; height: 520px;
    background: linear-gradient(to bottom, var(--flag-green) 0%, rgba(47,107,69,.75) 50%, rgba(47,107,69,0) 100%); }
  .flag-band--white { left: 250px; width: 357px; height: 560px;
    background: linear-gradient(to bottom, var(--flag-white) 0%, rgba(110,110,112,.55) 45%, rgba(60,60,62,0) 100%); }
  .flag-band--red { left: 607px; width: 241px; height: 760px;
    background: linear-gradient(to bottom, var(--flag-red) 0%, rgba(138,58,44,.7) 45%, rgba(110,45,35,0) 100%); }
  .stage-photo { position: absolute; left: 340px; top: 500px; width: 508px; height: 700px;
    background: radial-gradient(ellipse at 70% 45%, var(--photo-mid) 0%, rgba(31,42,68,.7) 40%, rgba(12,12,14,0) 75%),
                linear-gradient(to bottom, rgba(58,42,40,0) 0%, var(--photo-top) 35%, var(--photo-low) 100%); }
  .title { position: absolute; left: 0; width: 100%; top: 92px; text-align: center;
    font-family: "Cormorant Garamond", Georgia, serif; font-weight: 600; font-size: 190px; line-height: 1; color: var(--text-light); }
  .title-rule { position: absolute; left: 49px; top: 266px; width: 756px; height: 4px; border-radius: 2px;
    background: linear-gradient(to right, rgba(34,140,70,0) 0%, #22a04f 20%, #dfe9e2 50%, #e6463c 80%, rgba(230,70,60,0) 100%); }
  .subtitle { position: absolute; left: 0; width: 100%; top: 292px; text-align: center;
    font-weight: 500; font-size: 40px; line-height: 41px; color: var(--text-light); }
  .artist { position: absolute; left: 75px; top: 566px; font-weight: 400; font-size: 39px; line-height: 47px; color: var(--text-soft); }
  .event { position: absolute; left: 71px; top: 880px; width: 282px; }
  .event-date { font-weight: 700; font-size: 94px; line-height: 86px; letter-spacing: -3px; color: var(--text-soft); }
  .event-meta { display: flex; justify-content: space-between; font-size: 27px; line-height: 30px; color: var(--text-soft); }
  .event-rule { height: 4px; background: var(--text-light); margin-top: 10px; }
  .event-city { text-align: center; font-weight: 700; font-size: 86px; line-height: 82px; letter-spacing: 4px; margin-top: 8px; }
  .event-venue { text-align: center; font-weight: 500; font-size: 66px; line-height: 62px; }
</style>
</head>
<body>
  <main class="poster">
    <div class="flag-band flag-band--green"></div>
    <div class="flag-band flag-band--white"></div>
    <div class="flag-band flag-band--red"></div>
    <div class="stage-photo" role="img" aria-label="Foto des Musikers am Flügel mit Mikrofon, dunkelblaues Sakko, warmes Bühnenlicht"></div>

    <h1 class="title">Ventoro</h1>
    <div class="title-rule"></div>
    <p class="subtitle">Ein musikalischer Rückblick eines<br>italienischen Musikers</p>

    <p class="artist">MATTEO<br>VARLANI</p>

    <section class="event">
      <div class="event-date">XX.XX.</div>
      <div class="event-meta"><span>202X</span><span>00:00 UHR</span></div>
      <div class="event-rule"></div>
      <div class="event-city">STADT</div>
      <div class="event-venue">VENUE</div>
    </section>
  </main>
</body>
</html>
```